High end boutique food product label

We are looking for a label design to be used on our range of high end food products. We don't have a design or colour scheme in mind and are interested to see what ideas are submitted.
We would like it to feel sophisticated, chic, and eye-catching.
All of our products are handmade in Australia using Australian ingredients.
The graphics for the label will need to be scaleable to be fit a variety of labels from small squat jars with labels sized 3.5cm high and 7cm wide, to tall thin bottles with labels that are 14cm high and 4.5cm wide.
We would be interested in working with the winning designer to create these different sized labels.
The label submitted for this project should be 14cm high and 4.5cm wide, it should include our logo (file supplied in .jpeg and .ai), the product name 'Extra Virgin Olive Oil' and the size '250ml'.
This is just the front label on a bottle, we are not expecting a rear label to be created currently.
You are welcome to use any fonts you think will look good but the fonts used in our logo are Allaina Medium and Bebas Kai Regular.

```html
<!DOCTYPE html>
<html lang="en">
<head>
<meta charset="utf-8">
<title>Extra Virgin Olive Oil – Front Label</title>
<link href="https://fonts.googleapis.com/css2?family=Montserrat:wght@400;500;600&family=Great+Vibes&display=swap" rel="stylesheet">
<style>
  :root {
    --page-bg: #ececec;
    --cocoa: #45281a;
    --gold: #b49a74;
    --cream: #ffffff;
    --leaf-light: #eef7c6;
    --leaf-mid: #dfe9a6;
    --ink: #3a2a22;
    --olive-ink: #3d4a33;
    --branch: #8f9a3a;
  }
  * { box-sizing: border-box; margin: 0; padding: 0; }
  html, body {
    width: 1200px;
    height: 1027px;
    overflow: hidden;
    background: var(--page-bg);
  }
  .canvas {
    position: relative;
    width: 1200px;
    height: 1027px;
  }
  .label {
    position: absolute;
    left: 455px;
    top: 63px;
    width: 290px;
    height: 900px;
    overflow: hidden;
    background: radial-gradient(ellipse at 50% 62%, var(--leaf-light) 0%, var(--leaf-mid) 85%);
    box-shadow: 0 6px 22px rgba(0,0,0,0.18);
  }
  .label__crest {
    position: absolute;
    left: 0;
    top: 0;
    width: 290px;
    height: 390px;
  }
  .brand {
    position: absolute;
    top: 150px;
    left: 0;
    width: 100%;
    text-align: center;
    font-family: "Montserrat", sans-serif;
    font-weight: 600;
    color: var(--cream);
    font-size: 30px;
    line-height: 1.15;
    letter-spacing: 0.5px;
  }
  .product {
    position: absolute;
    top: 484px;
    left: 0;
    width: 100%;
    text-align: center;
  }
  .product__grade {
    font-family: "Montserrat", sans-serif;
    font-weight: 400;
    font-size: 19px;
    letter-spacing: 1.5px;
    color: var(--ink);
  }
  .product__name {
    font-family: "Great Vibes", cursive;
    font-size: 66px;
    line-height: 1;
    margin-top: 8px;
    color: var(--olive-ink);
  }
  .branch-art {
    position: absolute;
    left: 38px;
    top: 626px;
    width: 214px;
    height: 74px;
    border-radius: 40px;
    background: linear-gradient(90deg, rgba(143,154,58,0.15), rgba(143,154,58,0.45) 50%, rgba(143,154,58,0.15));
  }
  .volume {
    position: absolute;
    top: 774px;
    left: 0;
    width: 100%;
    text-align: center;
    font-family: "Montserrat", sans-serif;
    font-weight: 600;
    font-size: 22px;
    color: var(--ink);
  }
  .foliage-art {
    position: absolute;
    left: 0;
    bottom: 0;
    width: 100%;
    height: 88px;
    background: linear-gradient(180deg, rgba(143,154,58,0) 0%, rgba(143,154,58,0.28) 100%);
  }
</style>
</head>
<body>
<main class="canvas">
  <section class="label">
    <svg class="label__crest" viewBox="0 0 290 390" aria-hidden="true">
      <path d="M0 0 H290 V245 A145 145 0 0 1 0 245 Z" fill="var(--cocoa)"/>
      <path d="M15 0 V245 A130 128 0 0 0 275 245 V0" fill="none" stroke="var(--gold)" stroke-width="2"/>
    </svg>
    <div class="brand">Kestrel Grove<br>Pantry</div>

    <div class="product">
      <p class="product__grade">EXTRA VIRGIN</p>
      <h1 class="product__name">Olive Oil</h1>
    </div>

    <div class="branch-art" role="img" aria-label="Pair of olive branches with dark olives"></div>

    <p class="volume">250ml</p>

    <div class="foliage-art" role="img" aria-label="Border of sketched olive leaves and fruit"></div>
  </section>
</main>
</body>
</html>
```